Very Simple/Minimal Business Card Design Project

The company operates in the industrial maritime infrastructure sector in Brazil. You can find more information on our website www.navortek.com.br WE NEED TO LOOK POWERFUL AND SERIOUS
I have attached a copy of the old cards. We would like something more professional / industrial / sexy that also includes the position.

The card can be double sided or not. We would like you to propose as many options.

Thank you
Updates

Many thanks, do let me know if you have any questions. I am under a lot of time pressure to try and have them printed over the next days or so.

Please could you use the following information

for the address: Rua Tapiraçu, 417 - Centro, Rio de Janeiro, 20034-118, Brasil

for the mobile: +55 21 8237 9412
for the landline: +55 21 4096 3578

and position:  Diretor Geral

Thakn you

Target Market(s)

Shipowners, bankers, industrial companies

Industry/Entity Type

Industrial

Requirements
Must have
• POWERFUL
SERIOUS
SOLID
BIG CORPORATION

```html
<!DOCTYPE html>
<html lang="pt-BR">
<head>
<meta charset="utf-8">
<title>Navortek – Cartão de Visita</title>
<link rel="stylesheet" href="https://fonts.googleapis.com/css2?family=Open+Sans:wght@400;600;700&display=swap">
<style>
  :root {
    --navy: #22306b;
    --green: #1e9a48;
    --white: #ffffff;
    --backdrop: #eeeae4;
    --shadow: rgba(0, 0, 0, 0.35);
  }
  * { box-sizing: border-box; margin: 0; padding: 0; }
  html, body {
    width: 1200px; height: 1000px; overflow: hidden;
    background: var(--backdrop);
    font-family: "Open Sans", Arial, sans-serif;
  }
  .canvas { position: relative; width: 1200px; height: 1000px; }

  .card {
    position: absolute;
    top: 350px;
    width: 538px; height: 298px;
    background: var(--white);
    box-shadow: 5px 6px 8px var(--shadow);
    overflow: hidden;
  }

  /* Front side */
  .card--front { left: 45px; }
  .card--front .edge-strip {
    position: absolute; left: 0; top: 0; bottom: 0; width: 7px;
    background: var(--green);
  }
  .brand-vertical {
    position: absolute; left: 110px; top: 22px;
    width: 50px; height: 250px;
    display: flex; flex-direction: column; align-items: center; justify-content: flex-end;
    gap: 8px;
  }
  .brand-vertical .brand-name {
    writing-mode: vertical-rl;
    transform: rotate(180deg);
    font-weight: 700; font-size: 30px; letter-spacing: 0.5px;
    color: var(--navy); line-height: 1;
  }
  .brand-mark {
    width: 47px; height: 47px; border-radius: 4px;
    background: var(--green);
  }
  .info-panel {
    position: absolute; left: 270px; top: 0; right: 0; bottom: 0;
    background: var(--navy); color: var(--white);
  }
  .holder { position: absolute; top: 64px; left: 0; right: 0; text-align: center; }
  .holder-name { font-weight: 600; font-size: 18px; line-height: 1.2; }
  .holder-role { font-weight: 600; font-size: 14px; margin-top: 6px; }
  .contacts { position: absolute; left: 15px; top: 184px; list-style: none; font-size: 12px; }
  .contacts li { display: flex; align-items: flex-start; margin-bottom: 9px; line-height: 16px; }
  .contacts svg { width: 16px; height: 16px; margin-right: 22px; flex: none; fill: var(--white); }

  /* Back side */
  .card--back { left: 618px; width: 536px; }
  .card--back .edge-left {
    position: absolute; left: 0; top: 0; bottom: 0; width: 7px; background: var(--navy);
  }
  .card--back .edge-right {
    position: absolute; right: 0; top: 0; bottom: 0; width: 6px; background: var(--green);
  }
  .brand-centered {
    position: absolute; left: 160px; top: 127px;
    display: flex; align-items: center; gap: 5px;
  }
  .brand-centered .brand-mark { width: 42px; height: 42px; }
  .brand-centered .brand-name {
    font-weight: 700; font-size: 27px; color: var(--navy); letter-spacing: 0.5px;
  }
</style>
</head>
<body>
<main class="canvas">

  <section class="card card--front" aria-label="Frente do cartão">
    <div class="edge-strip"></div>
    <div class="brand-vertical">
      <span class="brand-name">NAVORTEK</span>
      <span class="brand-mark"></span>
    </div>
    <div class="info-panel">
      <div class="holder">
        <p class="holder-name">Rafael Monteiro</p>
        <p class="holder-role">Diretor Geral</p>
      </div>
      <ul class="contacts">
        <li>
          <svg viewBox="0 0 16 16" aria-hidden="true"><rect x="1" y="3" width="10" height="12" rx="1"/><rect x="12" y="1" width="3" height="14" rx="1"/></svg>
          <span>+55 21 4096 3578</span>
        </li>
        <li>
          <svg viewBox="0 0 16 16" aria-hidden="true"><path d="M5 1h6a1 1 0 0 1 1 1v12a1 1 0 0 1-1 1H5a1 1 0 0 1-1-1V2a1 1 0 0 1 1-1zm1 2v6h4V3z"/></svg>
          <span>+55 21 8237 9412</span>
        </li>
        <li>
          <svg viewBox="0 0 16 16" aria-hidden="true"><path d="M8 2 1 8h2v6h4v-4h2v4h4V8h2z"/></svg>
          <span>Rua Tapiraçu, 417 - Centro<br>Rio de Janeiro, 20034-118, Brasil</span>
        </li>
      </ul>
    </div>
  </section>

  <section class="card card--back" aria-label="Verso do cartão">
    <div class="edge-left"></div>
    <div class="edge-right"></div>
    <div class="brand-centered">
      <span class="brand-mark"></span>
      <span class="brand-name">NAVORTEK</span>
    </div>
  </section>

</main>
</body>
</html>
```